Eye-catching & Glamorous Labels for Skincare Bottles & Jars

We need new labels designed for our product range as we have been dormant for a few years and are now rebranding Velora Grace - Kindly Made Skincare. The label sizes are defined in the attached word document. All products have either a bright silver or a matte silver lid pump/spray so please keep this in mind.

We are open to colours and invite you to create bright trendy labels which are coordinated with the logo attached. The logo is not of any specific colour so dark on light, light on dark, tone on tone - we like purple / duck egg blue / turquoise WITH matte silver, however stronger colours like navy plus maroon with matte silver is also a strong favourite. If you feel inspired by a colour you think would be appropriate to Velora Grace please feel free to have a go.

A front section for product information is required and the back should include relevant details ie ingredients, company info, and a note that there has been no testing on animals.

The serum bottle will require a front and back label on a clear label in a pale colour to coordinate with the rest of the range. Size for this label is 35mm top edge, 25mm bottom edge, height 45mm - I have attached a picture of the serum bottle as they were originally pad printed. Please don't hesitate to contact me for any further information. Good luck!

Target Market(s)

Educated professional women 30-45 who are regular skincare users and looking for beautiful skincare products without animal derived ingredients and animal testing

Industry/Entity Type

Skin Care Product

Font styles to use
Serif
Sans Serif
Decorative
Script

Colors

Designer to choose colors to be used in the design.

Requirements
Must have
• Velora Grace Logo - eye catching design - not too busy or cramped.
Nice to have
• Is it possible to create a background pattern using a very small image of the logo? Just a thought.

```html
<!DOCTYPE html>
<html lang="en">
<head>
<meta charset="utf-8">
<title>Velora Grace – Day &amp; Night Cream Label</title>
<link rel="stylesheet" href="https://fonts.googleapis.com/css2?family=Encode+Sans+Semi+Condensed:wght@400;500&family=Encode+Sans:wght@400;500&display=swap">
<style>
  :root {
    --page-bg: #f4f3f4;
    --label-top: #6ed3d1;
    --label-mid: #37b5b3;
    --label-bottom: #14807f;
    --ink: #111416;
  }
  html, body {
    margin: 0;
    padding: 0;
    width: 1200px;
    height: 1200px;
    overflow: hidden;
    background: var(--page-bg);
  }
  .canvas {
    position: relative;
    width: 1200px;
    height: 1200px;
  }
  .label {
    position: absolute;
    left: 360px;
    top: 70px;
    width: 480px;
    height: 1060px;
    border-radius: 6px;
    background: linear-gradient(180deg, var(--label-top) 0%, var(--label-mid) 55%, var(--label-bottom) 100%);
    color: var(--ink);
    font-family: "Encode Sans", sans-serif;
    text-align: center;
  }
  .brand {
    position: absolute;
    top: 190px;
    left: 0;
    width: 100%;
  }
  .brand-mark {
    display: block;
    width: 64px;
    height: 64px;
    margin: 0 auto 26px;
    border-radius: 50%;
    background: var(--ink);
  }
  .brand-name {
    margin: 0;
    font-size: 30px;
    font-weight: 500;
    letter-spacing: 0.5px;
    text-transform: uppercase;
  }
  .brand-tagline {
    margin: 6px 0 0;
    font-size: 20px;
    font-weight: 400;
  }
  .product-title {
    position: absolute;
    top: 455px;
    left: 0;
    width: 100%;
    margin: 0;
    font-weight: 400;
    text-transform: uppercase;
    line-height: 1.2;
  }
  .product-title-line {
    display: block;
    font-size: 34px;
    letter-spacing: 1px;
  }
  .product-title-sub {
    display: block;
    margin-top: 6px;
    font-size: 38px;
    letter-spacing: 16px;
    padding-left: 16px;
  }
  .product-details {
    position: absolute;
    top: 720px;
    left: 0;
    width: 100%;
    font-family: "Encode Sans Semi Condensed", sans-serif;
  }
  .product-line {
    margin: 0;
    font-size: 20px;
  }
  .product-type {
    display: inline-block;
    margin: 22px 0 0;
    padding: 0 6px 4px;
    font-size: 42px;
    font-weight: 400;
    border-bottom: 1.5px solid var(--ink);
  }
  .product-claim {
    margin: 6px 0 0;
    font-size: 22px;
  }
  .product-volume {
    position: absolute;
    top: 1000px;
    left: 0;
    width: 100%;
    margin: 0;
    font-family: "Encode Sans Semi Condensed", sans-serif;
    font-size: 17px;
  }
</style>
</head>
<body>
<main class="canvas">
  <section class="label">
    <header class="brand">
      <span class="brand-mark"></span>
      <h1 class="brand-name">Velora Grace</h1>
      <p class="brand-tagline">Kindly Made Skincare</p>
    </header>

    <h2 class="product-title">
      <span class="product-title-line">Day &amp; Night</span>
      <span class="product-title-sub">Cream</span>
    </h2>

    <div class="product-details">
      <p class="product-line">Anti Aging Arsenal</p>
      <h3 class="product-type">Oil Serum</h3>
      <p class="product-claim">Sheer indulgence</p>
    </div>

    <p class="product-volume">30ml</p>
  </section>
</main>
</body>
</html>
```